Premium Personal Brand — Facebook Banner (Used Across All Platforms)

Update — Additional Color Direction
In addition to the dark charcoal/slate direction already described, I'm also interested in seeing variants with:
Dark navy blue — Deep, authoritative, intelligence-community feel. Same textured/matte treatment, not flat or bright.
Warm charcoal with steel blue accent — Keep the dark base but introduce a subtle steel blue gradient, accent line, or tonal shift. Sophisticated, modern, adds dimension without adding color noise.
Both should maintain the same premium, restrained, architectural feel described in the original brief. No bright blues, no corporate PowerPoint energy — think midnight, think depth, think weight.
Everything else in the brief remains the same.
I am building a premium personal brand as an executive advisor to founders ($5M+ revenue).
This contest is Facebook-banner–focused, but the design must represent a visual system that will be reused across:
- LinkedIn
- YouTube
I- nstagram
- X (Twitter)
- Website hero sections and other brand touchpoints
Think of the Facebook banner as the primary expression of the brand — not a one-off graphic.
This project is about discovering a high-end visual style and brand feel, not decoration.
What to design
Please submit one cohesive visual system, shown primarily as:
- Facebook banner (primary focus)
The same design language should clearly translate to all platforms listed above.
Designers are responsible for using the current recommended dimensions for each platform.
Quick clarification on background direction:
Backgrounds should have depth and texture, not flat color fields. Avoid pure white, light grey, or solid black backgrounds. Think matte, architectural materials — stone, graphite, concrete, steel — not blank canvases. Subtle tonal variation is encouraged. Obvious gradients or decorative patterns are not.
Text to use
Primary Headline:
- Your Business Is Too Valuable To Be Run On Hope.
Subheadline:
- You didn’t build a business to become its prisoner.
Name:
Paul Whitaker
The headline should be the dominant visual element.
Logo note (important)
My personal logo is currently being finalized.
For this contest:
- Use a simple “PW” monogram placeholder
- Clean, bold, geometric sans-serif
- Do not design a logo
- The winning design must allow an easy logo swap later.
Headshot note (important)
- Please do not include a headshot in the banner design.
- Most platforms display a circular profile image separately.
- The banner should stand on its own using typography, layout, and tone only.
- Design the banner assuming the profile photo will sit nearby, not inside the banner.
Style direction
The design should feel:
- Premium
- Calm
- Confident
- Restrained
- High-trust
- Dark, neutral backgrounds are preferred.
- Fewer elements are better than more.
Think:
- Owner-level advisor
- Private equity / boardroom tone
- Industrial, Modern, Minimalist, Elite, Architectural, not decorative
What to avoid
Please do not submit designs that feel:
- Promotional, hype-driven, or salesy
- Like a coach, guru, or agency
- Bright, colorful, or gradient-heavy
- Busy or over-designed
- Based on stock photos
- No motivational speaker energy.
Reaction test
- If someone sees this banner on Facebook (or later on LinkedIn, YouTube, etc.), the reaction should be:
“That person is serious. I’d trust them with important decisions.”
Final note
- I am not looking for many variations.
- I am looking for one strong visual direction you believe in.
Simple beats clever.
- Restraint beats decoration.

```html
<!DOCTYPE html>
<html lang="en">
<head>
<meta charset="utf-8">
<title>Paul Whitaker — Banner</title>
<link href="https://fonts.googleapis.com/css2?family=Montserrat:ital,wght@0,200;1,900&display=swap" rel="stylesheet">
<style>
  :root {
    --page: #2a2a2a;
    --banner-deep: #0b0b0c;
    --banner-mid: #1c1b1b;
    --banner-glow: #2a2827;
    --rule: rgba(255,255,255,0.12);
    --ink: #ffffff;
    --ink-soft: #e9e9e9;
  }
  * { margin: 0; padding: 0; box-sizing: border-box; }
  html, body {
    width: 1200px; height: 588px; overflow: hidden;
    background: var(--page);
  }
  .banner {
    position: absolute; left: 30px; top: 83px;
    width: 1140px; height: 422px;
    border-radius: 6px; overflow: hidden;
    background:
      radial-gradient(ellipse 60% 55% at 50% 48%, var(--banner-glow) 0%, rgba(0,0,0,0) 75%),
      linear-gradient(180deg, var(--banner-deep) 0%, var(--banner-mid) 30%, var(--banner-mid) 70%, var(--banner-deep) 100%);
  }
  .texture {
    position: absolute; inset: 0;
    background: linear-gradient(90deg, rgba(0,0,0,0.35) 0%, rgba(255,255,255,0.02) 50%, rgba(0,0,0,0.35) 100%);
  }
  .monogram {
    position: absolute; left: 44px; top: 28px;
    font: 200 40px/1 "Montserrat", sans-serif;
    color: var(--ink); letter-spacing: 6px;
  }
  .rule { position: absolute; left: 0; width: 100%; }
  .rule-top { top: 95px; }
  .rule-bottom { top: 339px; }
  .headline {
    position: absolute; left: 0; right: 0; top: 129px;
    text-align: center;
    font: italic 900 40px/49px "Montserrat", sans-serif;
    color: var(--ink); letter-spacing: 0.2px;
  }
  .subheadline {
    position: absolute; left: 0; right: 0; top: 259px;
    text-align: center;
    font: 200 32px/1 "Montserrat", sans-serif;
    color: var(--ink-soft);
  }
  .signature {
    position: absolute; right: 47px; top: 362px;
    font: italic 900 33px/1 "Montserrat", sans-serif;
    color: var(--ink);
  }
</style>
</head>
<body>
  <section class="banner">
    <div class="texture" role="img" aria-label="Subtle dark graphite texture"></div>

    <div class="monogram">PW</div>

    <svg class="rule rule-top" width="1140" height="4" viewBox="0 0 1140 4" aria-hidden="true">
      <defs>
        <linearGradient id="flare" x1="0" x2="1" y1="0" y2="0">
          <stop offset="0" stop-color="#ffffff" stop-opacity="0.08"/>
          <stop offset="0.7" stop-color="#ffffff" stop-opacity="0.12"/>
          <stop offset="0.84" stop-color="#f3e6d4" stop-opacity="0.95"/>
          <stop offset="0.93" stop-color="#ffffff" stop-opacity="0.12"/>
          <stop offset="1" stop-color="#ffffff" stop-opacity="0.05"/>
        </linearGradient>
      </defs>
      <rect x="0" y="1" width="1140" height="2" fill="url(#flare)"/>
    </svg>

    <h1 class="headline">Your Business Is Too Valuable<br>To Be Run On Hope.</h1>

    <p class="subheadline">You didn’t build a business to become its prisoner.</p>

    <svg class="rule rule-bottom" width="1140" height="2" viewBox="0 0 1140 2" aria-hidden="true">
      <rect x="0" y="0" width="1140" height="1" fill="var(--rule)"/>
    </svg>

    <div class="signature">Paul Whitaker</div>
  </section>
</body>
</html>
```